Business Card for Jewelry Business

We need a new namecard design for a jewelry company based in Bangkok, Thailand. We have a new website recently and want the new namecard to reflect our new modern image. I have uploaded our old namecard to show you the information that needs to be on the namecard. Pls check our website www.qelburn.com for the new color scheme to help design the new namecard.

```html
<!DOCTYPE html>
<html lang="en">
<head>
<meta charset="utf-8">
<title>Qelburn Business Card</title>
<link rel="stylesheet" href="https://fonts.googleapis.com/css2?family=Open+Sans:ital,wght@0,400;0,600;0,700;1,700&display=swap">
<style>
  :root {
    --bg: #8a8689;
    --card-white: #ffffff;
    --ink: #3a3a3c;
    --ink-soft: #555558;
    --aqua: #6fd9dc;
    --teal-dark: #1f4f55;
    --teal-mid: #1f7a80;
    --teal-light: #2aa3a8;
    --line: #6b6b6e;
  }
  * { box-sizing: border-box; margin: 0; padding: 0; }
  html, body { width: 1200px; height: 876px; overflow: hidden; }
  body {
    background: var(--bg);
    font-family: "Open Sans", Arial, sans-serif;
    color: var(--ink);
    position: relative;
  }
  .card {
    position: absolute;
    top: 268px;
    width: 540px;
    height: 340px;
    border-radius: 30px;
    overflow: hidden;
  }
  .card-front { left: 40px; background: var(--card-white); }
  .card-back {
    left: 620px;
    background: linear-gradient(120deg, var(--teal-dark) 0%, var(--teal-mid) 55%, var(--teal-light) 100%);
  }

  .holder { position: absolute; left: 40px; top: 30px; }
  .holder-name {
    font-weight: 700;
    font-size: 24px;
    letter-spacing: 6px;
    text-transform: uppercase;
  }
  .holder-title { font-size: 11px; letter-spacing: 0.4px; margin-top: 2px; color: var(--ink-soft); }
  .holder-bar { width: 280px; height: 7px; background: var(--aqua); margin-top: 6px; }

  .contacts { position: absolute; left: 40px; top: 110px; list-style: none; }
  .contact { display: flex; align-items: flex-start; gap: 10px; font-size: 12px; line-height: 1.35; margin-bottom: 9px; }
  .contact svg { width: 14px; height: 14px; flex: none; margin-top: 1px; }

  .divider { position: absolute; left: 30px; right: 30px; top: 282px; height: 1px; background: var(--line); }
  .social { position: absolute; top: 292px; display: flex; align-items: center; gap: 8px; font-size: 12px; }
  .social-facebook { left: 30px; }
  .social-instagram { right: 30px; }
  .social-dot { width: 14px; height: 14px; border-radius: 50%; background: var(--aqua); }

  .company { position: absolute; right: 34px; top: 180px; text-align: right; }
  .company-name { font-weight: 700; font-size: 19px; color: var(--ink); }
  .company-tag { font-size: 11.5px; letter-spacing: 1px; text-transform: uppercase; line-height: 1.4; margin-top: 6px; color: var(--ink-soft); }

  .brand-faint {
    position: absolute; right: 40px; top: 120px;
    font-size: 44px; font-weight: 600; color: #ece9e6;
  }

  .back-emblem {
    position: absolute; left: 50%; top: 50%;
    width: 200px; height: 200px; margin: -100px 0 0 -100px;
    border: 1.5px solid #ffffff; border-radius: 50%;
    display: flex; align-items: center; justify-content: center;
  }
  .back-name { color: #ffffff; font-size: 30px; font-weight: 600; letter-spacing: 1px; }
</style>
</head>
<body>
  <section class="card card-front" aria-label="Card front">
    <div class="brand-faint">Qelburn</div>

    <header class="holder">
      <div class="holder-name">Nara Phetsiri</div>
      <div class="holder-title">Sales &amp; Product Development Manager</div>
      <div class="holder-bar"></div>
    </header>

    <ul class="contacts">
      <li class="contact">
        <svg viewBox="0 0 24 24"><path fill="#6fd9dc" d="M12 2a7 7 0 0 0-7 7c0 5 7 13 7 13s7-8 7-13a7 7 0 0 0-7-7zm0 9.5A2.5 2.5 0 1 1 12 6.5a2.5 2.5 0 0 1 0 5z"/></svg>
        <span>142 Moo 7 Suwinthawong Road,<br>Nong Chok Industrial Park,<br>Bangkok, 10530 Thailand</span>
      </li>
      <li class="contact">
        <svg viewBox="0 0 24 24"><path fill="#6fd9dc" d="M6.6 10.8a15 15 0 0 0 6.6 6.6l2.2-2.2a1 1 0 0 1 1-.25 11.4 11.4 0 0 0 3.6.57 1 1 0 0 1 1 1V20a1 1 0 0 1-1 1A17 17 0 0 1 3 4a1 1 0 0 1 1-1h3.5a1 1 0 0 1 1 1c0 1.25.2 2.45.57 3.6a1 1 0 0 1-.25 1z"/></svg>
        <span>+662-418-0273</span>
      </li>
      <li class="contact">
        <svg viewBox="0 0 24 24"><circle cx="12" cy="12" r="4" fill="none" stroke="#6fd9dc" stroke-width="2.5"/><path d="M16 8v5a2.5 2.5 0 0 0 5 0v-1a9 9 0 1 0-4 7.5" fill="none" stroke="#6fd9dc" stroke-width="2.5"/></svg>
        <span>hello@qelburn.com</span>
      </li>
      <li class="contact">
        <svg viewBox="0 0 24 24"><g fill="none" stroke="#6fd9dc" stroke-width="2"><circle cx="12" cy="12" r="9"/><path d="M3 12h18M12 3c3 3 3 15 0 18M12 3c-3 3-3 15 0 18"/></g></svg>
        <span>www.qelburn.com</span>
      </li>
    </ul>

    <div class="company">
      <div class="company-name">Qelburn Co., Ltd</div>
      <div class="company-tag">Manufacturers of fine<br>gold &amp; silver jewelry</div>
    </div>

    <div class="divider"></div>
    <div class="social social-facebook"><span class="social-dot"></span><span>Qelburn Jewelry</span></div>
    <div class="social social-instagram"><span class="social-dot"></span><span>@QelburnJewelry</span></div>
  </section>

  <section class="card card-back" aria-label="Card back">
    <div class="back-emblem"><span class="back-name">Qelburn</span></div>
  </section>
</body>
</html>
```